Front & Back Book Cover Design

Title:
THE QUIET LANDLORD: How to Grow Comfort and Plenty Through Property Held by Others
Author:
Mel T. Varnak
Design Philosophy:
A modern, minimalist-luxury aesthetic that feels visionary and intelligent — positioned between business innovation (The Brisk Venture), modern finance (The Anatomy of Thrift), and timeless real estate insight (Bold Aunt Meek Aunt).
Think: clean, bold, and idea-driven — a visual reflection of the book’s central concept: wealth through clarity, not clutter.
Back Cover:
To include book description along with author photo and bio
Files:
PNG, PDF, EPUB

```html
<!DOCTYPE html>
<html lang="en">
<head>
<meta charset="utf-8">
<title>The Quiet Landlord — Cover Spread</title>
<link rel="stylesheet" href="https://fonts.googleapis.com/css2?family=Anton&family=Archivo+Black&family=Oswald:wght@600;700&family=Roboto+Condensed:wght@400;700&display=swap">
<style>
  :root {
    --canvas: #dde7e8;
    --blue: #0a7fc2;
    --dark: #13181d;
    --yellow: #fcc10e;
    --navy: #1e2a78;
    --accent-blue: #1b82cf;
    --white: #ffffff;
    --display: "Anton", "Oswald", sans-serif;
    --wide: "Archivo Black", sans-serif;
    --cond: "Oswald", sans-serif;
    --body: "Roboto Condensed", sans-serif;
  }
  * { margin: 0; padding: 0; box-sizing: border-box; }
  html, body { width: 814px; height: 1200px; overflow: hidden; background: var(--canvas); }
  .cover-spread {
    position: absolute; left: 27px; top: 324px;
    width: 760px; height: 552px;
    background: var(--blue); overflow: hidden;
    box-shadow: 0 6px 18px rgba(0,0,0,.18);
    font-family: var(--body); color: var(--white);
  }
  .spread-backdrop { position: absolute; inset: 0; }
  .abs { position: absolute; }

  /* Back cover */
  .back-title { left: 35px; top: 28px; }
  .back-title .the { font-family: var(--wide); color: var(--navy); font-size: 15px; line-height: 16px; }
  .back-title .line { font-family: var(--display); font-size: 33px; line-height: 31px; letter-spacing: .3px; }
  .back-subtitle {
    left: 185px; top: 76px;
    font-family: var(--cond); font-weight: 700; font-size: 10.5px; line-height: 11.6px; text-transform: uppercase;
  }
  .back-copy { left: 35px; top: 195px; width: 300px; }
  .question { color: var(--accent-blue); font-size: 9px; line-height: 11px; font-weight: 400; }
  .copy { font-size: 6.4px; line-height: 8.4px; margin-top: 7px; }
  .discover-head { color: var(--yellow); font-size: 8.5px; font-weight: 700; margin-top: 9px; }
  .benefits { list-style: none; margin-top: 6px; }
  .benefits li { font-size: 6.2px; line-height: 12.4px; padding-left: 9px; position: relative; }
  .benefits li::before {
    content: ""; position: absolute; left: 1px; top: 4.8px;
    width: 2.8px; height: 2.8px; border-radius: 50%; background: var(--yellow);
  }
  .hl { color: var(--accent-blue); }
  .closing { margin-top: 12px; padding-left: 2px; }

  .author-photo {
    left: 34px; top: 416px; width: 62px; height: 62px; border-radius: 50%;
    background: radial-gradient(circle at 50% 40%, #b89a86 0%, #6d5a50 55%, #2a2a2e 100%);
  }
  .author-bio { left: 108px; top: 418px; width: 230px; }
  .author-bio .bio-head { color: var(--yellow); font-size: 8.5px; font-weight: 400; }
  .author-bio p { font-size: 6.2px; line-height: 9px; margin-top: 3px; }

  /* Spine */
  .spine-author, .spine-title {
    left: 381px; transform-origin: center; white-space: nowrap;
  }
  .spine-author {
    top: 90px; transform: translate(-50%, -50%) rotate(-90deg);
    font-family: var(--cond); font-weight: 700; color: var(--yellow); font-size: 20px;
  }
  .spine-title {
    top: 385px; transform: translate(-50%, -50%) rotate(-90deg);
    font-family: var(--wide); font-size: 16px; letter-spacing: .3px;
  }

  /* Front cover */
  .front-title { left: 400px; width: 360px; top: 18px; text-align: center; }
  .front-title .the { font-family: var(--wide); color: var(--navy); font-size: 28px; line-height: 28px; }
  .front-title .line { font-family: var(--display); font-size: 62px; line-height: 56px; letter-spacing: .5px; }
  .front-art {
    left: 419px; top: 180px; width: 321px; height: 205px;
    background: linear-gradient(180deg, var(--blue) 0%, #0b5f93 45%, #1d3650 70%, var(--dark) 100%);
    border-radius: 0 0 40% 40% / 0 0 30% 30%;
  }
  .front-subtitle {
    left: 400px; width: 360px; top: 410px; text-align: center;
    font-family: var(--cond); font-weight: 700; font-size: 20px; line-height: 21.5px; text-transform: uppercase;
  }
  .front-author {
    left: 400px; width: 360px; top: 492px; text-align: center;
    font-family: var(--cond); font-weight: 700; color: var(--yellow); font-size: 29px; line-height: 34px;
  }
  .yellow { color: var(--yellow); }
  .white { color: var(--white); }
  .blue { color: var(--accent-blue); }
  .navy { color: var(--navy); }
</style>
</head>
<body>
<main class="cover-spread">
  <svg class="spread-backdrop" width="760" height="552" viewBox="0 0 760 552" aria-hidden="true">
    <path d="M0 217 L75 133 L170 134 L362 248 L362 552 L0 552 Z" fill="var(--dark)"/>
    <path d="M362 248 L400 255 L400 552 L362 552 Z" fill="var(--dark)"/>
    <path d="M400 230 L760 205 L760 552 L400 552 Z" fill="var(--dark)"/>
  </svg>

  <!-- Back cover -->
  <div class="abs back-title">
    <div class="the">THE</div>
    <div class="line yellow">QUIET</div>
    <div class="line white">LANDLORD</div>
  </div>
  <div class="abs back-subtitle">
    <div class="white">How to grow comfort &amp;</div>
    <div class="yellow">plenty through</div>
    <div class="yellow">property held by others</div>
  </div>

  <section class="abs back-copy">
    <h2 class="question">What if the smartest property investors in the<br>world don’t actually own anything?</h2>
    <p class="copy">In a world where leverage has replaced labor and access has replaced assets, The Quiet Landlord reveals how a new generation of entrepreneurs is building wealth without deeds, mortgages, or massive capital.<br>Mel T. Varnak exposes the hidden playbook behind modern property wealth — not through ownership, but through control, creativity, and influence.</p>
    <h3 class="discover-head">You’ll discover how to:</h3>
    <ul class="benefits">
      <li><span class="hl">Profit from properties you never buy</span> through partnerships, performance models, and control agreements.</li>
      <li><span class="hl">Monetize your skills, systems, and relationships</span> just like institutional investors do.</li>
      <li><span class="hl">Build digital real estate</span> - brands, websites, and lead funnels that pay like rentals.</li>
      <li><span class="hl">Create recurring income</span> through master leases, management contracts, and service-based equity.</li>
      <li><span class="hl">Design your freedom formula</span> - where wealth is measured in time, not titles.</li>
    </ul>
    <p class="copy closing">Packed with frameworks, examples, and the mindset of modern deal-makers, The Quiet Landlord is a blueprint for the future of wealth creation - one built on access, not assets.<br>Because in the new economy, <span class="hl">the most powerful investors don’t own property. They own opportunity.<br>And now, you can too.</span></p>
  </section>

  <div class="abs author-photo" role="img" aria-label="Author portrait photograph"></div>
  <section class="abs author-bio">
    <h3 class="bio-head">About the Author</h3>
    <p><span class="hl">Mel T. Varnak</span> is a property entrepreneur and owner of Halvern Studio in Marlow Springs, NV and Crestline Realty Partners in Seabrook, California. Combining design, development, and deal strategy, he’s helped agents, investors, and entrepreneurs build freedom through systems - not stuff. The Quiet Landlord is his definitive guide to building wealth through creative control.</p>
  </section>

  <!-- Spine -->
  <div class="abs spine-author">Mel T. Varnak</div>
  <div class="abs spine-title"><span class="yellow">THE</span> <span class="blue">QUIET</span> <span class="white">LANDLORD</span></div>

  <!-- Front cover -->
  <h1 class="abs front-title">
    <div class="the">THE</div>
    <div class="line yellow">QUIET</div>
    <div class="line white">LANDLORD</div>
  </h1>
  <div class="abs front-art" role="img" aria-label="Illustration of a climber scaling a giant golden key with a dollar sign, rising from a dark mountain crevasse"></div>
  <div class="abs front-subtitle">
    <div class="white">How to grow comfort &amp;</div>
    <div class="blue">plenty through</div>
    <div class="blue">property held by others</div>
  </div>
  <div class="abs front-author">Mel T. Varnak</div>
</main>
</body>
</html>
```